WAYmaker website redesign to provide information about experiential workshops, film work and other

We need a redesign of our website waymakerhub.org. We conduct experiential workshops of discovery and transformation for individuals and organizations. We need the website to reflect the full extent of WAYmaker programs, and be an information hub for WAYmaker workshops and communities as they develop.

The attached documents contain information about the organization - it's brandbook, copy for web pages, a website layout and a couple of images.

The site is for individuals and companies looking to promote and be change to make a difference. It should be warm, welcoming, and create excitement around the concepts and the ability to discover a new way of being in the world. We are about creating communities around the globe who will embody play, freedom, curiosity and expanded possibilities. We are creating a space for this to happen, both physically (workshops) and online.

We will be on either a SquareSpace, but mos tlikely a Weebly plaform.

Please look at the current site at www.waymakerhub.org

Target Market(s)

Initially, are target market will be baby boomers, but will expand to include millennials and students.

Coding

Coded - Design and coding required

Number of Pages Required

5+ page

Requirements
Must have
• The colors, logo and fonts from the brand book.
Nice to have
• Complimentary use of brand colors to create an attractive presentation and energy

```html
<!DOCTYPE html>
<html lang="en">
<head>
<meta charset="utf-8">
<title>WAYmaker — Experiential Workshops</title>
<link href="https://fonts.googleapis.com/css2?family=Poppins:wght@300;400;500;600;700&display=swap" rel="stylesheet">
<style>
:root{
  --orange:#f26a2e;
  --orange-deep:#c9531d;
  --ink:#1f1f1f;
  --teal:#0f3336;
  --cream:#f5f0ea;
  --light:#f7f7f7;
  --footer:#1b1b1b;
  --bar:#111;
  --white:#fff;
  --icon-soft:#fbe3d7;
}
*{box-sizing:border-box;margin:0;padding:0}
html,body{width:1200px;height:4018px;overflow:hidden}
body{font-family:'Poppins',sans-serif;color:var(--ink);position:relative;background:var(--white)}
.abs{position:absolute}
.btn{display:inline-flex;align-items:center;justify-content:center;border-radius:30px;background:var(--orange);color:var(--white);font-size:13px;font-weight:500}

/* header */
.topbar{top:0;left:0;width:1200px;height:107px;background:#262626}
.topbar .phone{left:85px;top:44px;color:var(--white);font-size:14px;display:flex;align-items:center;gap:8px}
.brand{left:420px;top:28px;width:360px;text-align:center;color:var(--white);font-size:44px;font-weight:700;letter-spacing:4px;display:flex;align-items:center;justify-content:center;gap:14px}
.brand i{width:18px;height:18px;background:var(--orange);display:block}
.topbar .b1{left:865px;top:34px;width:145px;height:40px}
.topbar .b2{left:1022px;top:34px;width:95px;height:40px}
.nav{top:107px;left:0;width:1200px;height:54px;background:var(--orange-deep);display:flex;justify-content:center;align-items:center;gap:42px;color:var(--white);font-size:14px}

/* hero */
.hero{top:161px;left:0;width:1200px;height:648px;background:linear-gradient(135deg,#6e5a48 0%,#4b3d33 45%,#2e2925 100%)}
.hero h1{left:85px;top:268px;color:var(--white);font-size:40px;font-weight:500;line-height:62px}

/* discover */
.discover{top:809px;left:0;width:1200px;height:504px;background:var(--cream)}
.discover .photo{left:0;top:0;width:540px;height:504px;background:linear-gradient(160deg,#5b5f63,#2f3236);clip-path:polygon(0 0,100% 0,450px 100%,0 100%)}
.discover h2{left:548px;top:80px;color:var(--orange);font-size:29px;font-weight:700;line-height:44px}
.discover .lead{left:548px;top:175px;font-size:15px;font-weight:600}
.ticks{left:548px;top:207px;list-style:none;font-size:15px;line-height:30px}
.ticks li{display:flex;align-items:center;gap:12px}
.tick{width:16px;height:16px;border-radius:50%;background:var(--orange);display:inline-flex;align-items:center;justify-content:center}
.discover .btn{left:548px;top:375px;width:145px;height:46px}

/* vision */
.vision{top:1313px;left:0;width:1200px;height:477px;background:var(--teal)}
.vision h2{left:105px;top:112px;color:var(--white);font-size:30px;font-weight:600}
.vision p{left:105px;top:165px;width:510px;color:#d7dede;font-size:15px;line-height:30px}
.vision .btn{left:105px;top:307px;width:142px;height:46px}
.vision .frame{left:870px;top:67px;width:250px;height:350px;background:var(--orange)}
.vision .photo{left:655px;top:90px;width:430px;height:305px;background:linear-gradient(135deg,#4f6b4a,#2d3b2a)}

/* what we do */
.what{top:1790px;left:0;width:1200px;height:630px;background:var(--light)}
.what h2{left:0;top:50px;width:1200px;text-align:center;color:var(--orange);font-size:30px;font-weight:700}
.what p{left:140px;top:105px;width:920px;text-align:center;font-size:15px;line-height:30px}
.what h3{left:0;top:228px;width:1200px;text-align:center;color:var(--orange);font-size:21px;font-weight:600;line-height:34px}
.cards{left:100px;top:345px;display:flex;gap:30px}
.card{width:175px;height:210px;background:var(--white);box-shadow:0 2px 10px rgba(0,0,0,.12);display:flex;flex-direction:column;align-items:center;padding-top:32px}
.movement-mark{width:96px;height:96px;border-radius:8px;background:radial-gradient(circle,var(--icon-soft) 0%,#f8c9b1 100%)}
.card span{margin-top:18px;color:var(--orange);font-weight:600;font-size:17px;text-align:center;line-height:24px}

/* workshop */
.peace{top:2420px;left:0;width:1200px;height:600px;background:var(--orange)}
.peace .frame{left:600px;top:80px;width:515px;height:440px;background:#1e1e1e}
.peace .photo{left:612px;top:92px;width:491px;height:416px;background:linear-gradient(180deg,#e6e6e6,#9b9b9b 60%,#5a5a5a)}
.peace .box{left:92px;top:120px;width:560px;height:355px;background:var(--white);padding:30px 48px}
.peace h2{color:var(--orange);font-size:29px;font-weight:700}
.peace p{margin-top:14px;font-size:15px;line-height:30px}
.peace .btn{margin-top:22px;width:142px;height:44px}

/* community */
.community{top:3020px;left:0;width:1200px;height:637px;background:var(--light)}
.community h2{left:0;top:40px;width:1200px;text-align:center;color:var(--orange);font-size:30px;font-weight:700}
.community .sub{left:0;top:100px;width:1200px;text-align:center;font-size:15px;line-height:30px;font-weight:500}
.field{background:var(--white);border:1px solid #ddd;font-size:14px;color:#666;padding:14px 18px}
.community .btn{left:535px;top:513px;width:165px;height:48px}

/* footer */
.footer{top:3657px;left:0;width:1200px;height:303px;background:var(--footer);color:#cfcfcf}
.footer h4{color:var(--white);font-size:21px;font-weight:500}
.footer p,.footer li{font-size:13px;line-height:26px;list-style:none}
.soc{display:flex;gap:14px;margin-top:22px}
.soc i{width:36px;height:36px;border-radius:50%;border:1px solid #555;display:block}
.copy{top:3960px;left:0;width:1200px;height:58px;background:var(--bar);color:#aaa;font-size:13px;text-align:center;line-height:58px}

/* subscription layer */
.dim{top:0;left:0;width:1200px;height:4018px;background:rgba(0,0,0,.72)}
.modal{left:107px;top:160px;width:986px;height:162px;background:var(--white)}
.modal h2{position:absolute;left:0;top:30px;width:986px;text-align:center;color:var(--orange);font-size:27px;font-weight:600}
.modal .field{position:absolute;top:90px;width:218px;height:40px;padding:9px 14px;font-size:13px;border:1px solid #ccc;box-shadow:0 1px 3px rgba(0,0,0,.2)}
.modal .send{position:absolute;left:748px;top:90px;width:215px;height:38px;background:var(--orange);color:var(--white);font-weight:600;font-size:15px;display:flex;align-items:center;justify-content:center;gap:8px}
</style>
</head>
<body>

<header class="topbar abs">
  <div class="phone abs"><svg width="16" height="16" viewBox="0 0 24 24"><path fill="#f26a2e" d="M6.6 10.8a15 15 0 0 0 6.6 6.6l2.2-2.2c.3-.3.7-.4 1-.2 1.1.4 2.3.6 3.6.6.6 0 1 .4 1 1V20c0 .6-.4 1-1 1A17 17 0 0 1 3 4c0-.6.4-1 1-1h3.5c.6 0 1 .4 1 1 0 1.3.2 2.5.6 3.6.1.3 0 .7-.2 1z"/></svg>Call us: (555) 014-2200</div>
  <div class="brand abs"><i></i>WAYMAKER</div>
  <a class="btn b1 abs">Find a Workshop</a>
  <a class="btn b2 abs">Login</a>
</header>
<nav class="nav abs"><span>Home</span><span>About Us</span><span>The Workshop</span><span>WAYmaker Life Projects</span><span>Films</span><span>Books &amp; Resources</span><span>Community</span><span>Contact Us</span></nav>

<section class="hero abs" role="img" aria-label="Photo of people in conversation in a warm wooden lounge">
  <h1 class="abs">What World Do We Want to Live In?<br>What Kind of Life Do You Want to Create?</h1>
</section>

<section class="discover abs">
  <div class="photo abs" role="img" aria-label="Photo of a group gathered outdoors by a timber building"></div>
  <h2 class="abs">DISCOVER AN OPPORTUNITY TO LIVE<br>A MORE DYNAMIC AND MEANINGFUL LIFE</h2>
  <div class="lead abs">WAYmaker:</div>
  <ul class="ticks abs">
    <li><span class="tick"><svg width="9" height="9" viewBox="0 0 10 10"><path d="M1 5l3 3 5-6" stroke="#fff" stroke-width="2" fill="none"/></svg></span>Renews Energy</li>
    <li><span class="tick"><svg width="9" height="9" viewBox="0 0 10 10"><path d="M1 5l3 3 5-6" stroke="#fff" stroke-width="2" fill="none"/></svg></span>Creates Opportunities for Connecting</li>
    <li><span class="tick"><svg width="9" height="9" viewBox="0 0 10 10"><path d="M1 5l3 3 5-6" stroke="#fff" stroke-width="2" fill="none"/></svg></span>Supports Conscious Evolution</li>
    <li><span class="tick"><svg width="9" height="9" viewBox="0 0 10 10"><path d="M1 5l3 3 5-6" stroke="#fff" stroke-width="2" fill="none"/></svg></span>Deepens Experience of Life</li>
    <li><span class="tick"><svg width="9" height="9" viewBox="0 0 10 10"><path d="M1 5l3 3 5-6" stroke="#fff" stroke-width="2" fill="none"/></svg></span>Provides Opportunities for Collaboration and Creation</li>
  </ul>
  <a class="btn abs">READ MORE</a>
</section>

<section class="vision abs">
  <h2 class="abs">VISSION</h2>
  <p class="abs">We envision a world in which all people and communities can challenge and break free from stories that no longer serve us. We believe that solutions to contemporary challenges will emerge from a place of curiosity, love and connection.</p>
  <a class="btn abs">READ MORE</a>
  <div class="frame abs"></div>
  <div class="photo abs" role="img" aria-label="Photo of two people talking seated before a forest window"></div>
</section>

<section class="what abs">
  <h2 class="abs">WHAT WE DO</h2>
  <p class="abs">WAYmaker Life is a workshop designed to re-engage you with life. Through interactive exercises and personal exploration, you are taken on a journey that ultimately leaves you experiencing life as a Creator. You will learn to see beliefs and patterns that hold you back in work and relationships as well as a path to transforming the story of your life.</p>
  <h3 class="abs">WAYMAKER LIFE IS A 3-4 DAY WORKSHOP<br>EXPERIENCED IN 5 MOVEMENTS</h3>
  <div class="cards abs">
    <div class="card"><div class="movement-mark" role="img" aria-label="Symbol for the Curiosity movement"></div><span>CURIOSITY</span></div>
    <div class="card"><div class="movement-mark" role="img" aria-label="Symbol for the Awareness movement"></div><span>AWARENESS</span></div>
    <div class="card"><div class="movement-mark" role="img" aria-label="Symbol for the Owning Your Creation movement"></div><span>OWNING YOUR CREATION</span></div>
    <div class="card"><div class="movement-mark" role="img" aria-label="Symbol for the Remaking movement"></div><span>REMAKING</span></div>
    <div class="card"><div class="movement-mark" role="img" aria-label="Symbol for the Manifesting movement"></div><span>MANIFESTING</span></div>
  </div>
</section>

<section class="peace abs">
  <div class="frame abs"></div>
  <div class="photo abs" role="img" aria-label="Photo of a workshop circle of seated participants in a bright room"></div>
  <div class="box abs">
    <h2>SHIFTING THE GROUND</h2>
    <p>The Shifting the Ground workshop—an extension of the documentary of the same name—is an experiential process to transform participants into disturbers of the status quo within themselves, to enhance their relationships with others, and to change the environments in which they learn—and ultimately society—for the better.</p>
    <a class="btn">READ MORE</a>
  </div>
</section>

<section class="community abs">
  <h2 class="abs">IN YOUR COMMUNITY</h2>
  <div class="sub abs">Bring WAYmaker or the Shifting the Ground workshop to your community.<br>We would love to hear from you.</div>
  <div class="field abs" style="left:240px;top:180px;width:355px;height:58px">Name</div>
  <div class="field abs" style="left:605px;top:180px;width:355px;height:58px">Phone Number</div>
  <div class="field abs" style="left:240px;top:248px;width:355px;height:58px">Email</div>
  <div class="field abs" style="left:605px;top:248px;width:355px;height:58px">Subject</div>
  <div class="field abs" style="left:240px;top:318px;width:720px;height:150px">Message</div>
  <a class="btn abs">SUBMIT</a>
</section>

<footer class="footer abs">
  <div class="abs" style="left:100px;top:60px;width:290px">
    <h4>ABOUT COMPANY</h4>
    <p style="margin-top:14px">WAYmaker hosts experiential workshops of discovery and transformation for people and groups seeking a new way to live.</p>
    <div class="soc"><i></i><i></i><i></i><i></i></div>
  </div>
  <div class="abs" style="left:408px;top:60px;width:220px">
    <h4>CONTACT US</h4>
    <ul style="margin-top:14px"><li>120 Maple Row, Riverton</li><li>hello@waymakerhub.org</li><li>(555) 014-2200</li></ul>
  </div>
  <div class="abs" style="left:652px;top:60px">
    <h4>QUICK LINKS</h4>
    <ul style="margin-top:14px"><li>Home</li><li>About Us</li><li>The Workshop</li><li>WAYmaker Life Projects</li><li>Films</li><li>Books &amp; Resources</li><li>Community</li></ul>
  </div>
  <div class="abs" style="left:878px;top:60px">
    <h4>QUICK LINKS</h4>
    <ul style="margin-top:14px"><li>Our Team</li><li>Events &amp; News</li><li>Gallery</li><li>Our Films</li><li>Testimonials</li><li>Contact Us</li></ul>
  </div>
</footer>
<div class="copy abs">Copyright © 2024 WAYmaker. All rights reserved.</div>

<div class="dim abs"></div>
<div class="modal abs">
  <h2>Email Subscription</h2>
  <div class="field" style="left:21px">First name</div>
  <div class="field" style="left:263px">Last Name</div>
  <div class="field" style="left:505px">Email address</div>
  <div class="send"><svg width="15" height="15" viewBox="0 0 24 24"><path fill="#fff" d="M2 11L22 2l-6 20-4-8z"/></svg>Submit</div>
</div>

</body>
</html>
```